Real Estate Site Update - wordpress

my wordpress site has not been updated in 6 years and needs a makeover
1. I would like to include my new logo (attached)
2. I would also like to include new staff photos (attached)
3. I would like to include client video testimonials (attached)
4. I would like to have real estate agent bio template pages for current and new agents
5. the site needs mobile device functionality
6. I would like a new look and more overall usability and functionality
Pages needed
1. main page
2. about us page
3. agent bio page template
4. 1st time buyer class sign up page - handbook purchase (paypal)
5. property search pages (lot finder)
6. first time buyer picture and announcement blog page
7. buyer information resources
8. seller information resources
I am looking for interesting Ideas on how to make my real estate website POP
current page is brightkeyrealty.com
I currently have and need
1. ability to post to social media (Activated)
2. I'd like to incorporate my youtube page brightkeyrealtyny
3. ability to register clients for class attendance (activated need presentation update)
4. ability to charge for class and booklets via paypal (activated)
5. ability to provide mls listing searches via lotfinder activated needs better presentation
if access to my current website file structure will assist please advise, i will gladly provide access
wordpress tools currently activated
QTRV
Post Stack
Gatemoat
Tablero
Snipo
Lot Finder
Target Market(s)
ages 22-50 income 30k and up
Industry/Entity Type
Real Estate

```html
<!DOCTYPE html>
<html lang="en">
<head>
<meta charset="utf-8">
<title>Brightkey Realty</title>
<link rel="stylesheet" href="https://fonts.googleapis.com/css2?family=Roboto:wght@400;500;700&family=Open+Sans:ital,wght@0,400;0,600;1,400&display=swap">
<style>
:root{
  --pink:#e85b7a;
  --pink-soft:#ef7d95;
  --dark:#1d242c;
  --dark-nav:#252d36;
  --ink:#2c2f33;
  --muted:#6b6f73;
  --line:#e3e3e3;
  --card-foot:#f1f1f1;
  --white:#fff;
}
*{margin:0;padding:0;box-sizing:border-box}
html,body{width:1200px;height:2844px;overflow:hidden}
body{font-family:"Open Sans",Arial,sans-serif;color:var(--ink);background:var(--white);position:relative}
.wrap{position:absolute;left:99px;width:1003px}

/* header */
.topbar{position:absolute;top:0;left:0;width:1200px;height:142px;background:var(--dark)}
.contact-top{position:absolute;left:99px;top:52px;display:flex;align-items:center;gap:12px;color:#fff;font-size:14px;line-height:19px}
.contact-top .icon{width:32px;height:32px;border-radius:50%;background:var(--pink);display:flex;align-items:center;justify-content:center}
.brand{position:absolute;left:0;width:1200px;top:44px;text-align:center;font-family:"Roboto",sans-serif;font-weight:500;font-size:34px;color:var(--pink);letter-spacing:1px}
.search{position:absolute;left:870px;top:54px;width:232px;height:36px;border:1px solid #59606a;border-radius:3px;color:#8a9098;font-size:12px;padding:10px 14px}
.search svg{position:absolute;right:12px;top:11px}

.nav{position:absolute;top:142px;left:0;width:1200px;height:53px;background:var(--dark-nav)}
.nav ul{list-style:none;position:absolute;left:99px;display:flex;height:53px}
.nav li{color:#fff;font-family:"Roboto",sans-serif;font-weight:500;font-size:13px;display:flex;align-items:center;padding:0 25px;border-right:1px solid #343c46}
.nav li.home{background:var(--pink);width:81px;justify-content:center;padding:0}

/* hero */
.hero{position:absolute;top:195px;left:0;width:1200px;height:554px;background:linear-gradient(180deg,#a9c3dd 0%,#8a8f86 35%,#6f6a5f 55%,#5f8a3c 78%,#4f7d2f 100%)}
.hero-caption{position:absolute;left:99px;top:188px;width:380px;height:208px;background:rgba(30,36,44,.72);padding:70px 18px 0}
.hero-caption h1{font-family:"Roboto",sans-serif;font-weight:700;font-size:44px;color:#fff;line-height:48px}
.hero-caption p{color:#fff;font-size:14px;line-height:22px;margin-top:10px}
.arrow{position:absolute;top:250px}
.quick{position:absolute;left:772px;top:0;width:328px;height:554px;background:rgba(255,255,255,.86)}
.quick-head{height:156px;background:var(--pink);text-align:center;color:#fff;padding-top:80px}
.quick-head h2{font-family:"Roboto",sans-serif;font-weight:500;font-size:26px;letter-spacing:1px}
.quick-head p{font-size:13px}
.field{position:absolute;left:34px;display:flex;align-items:center;font-size:13px;color:#333}
.field label{width:84px}
.field .box{width:178px;height:40px;border:1px solid #ddd;background:#fff;border-radius:2px;padding:11px 12px;font-size:13px;position:relative}
.field .box svg{position:absolute;right:12px;top:17px}
.quick .btn{position:absolute;left:120px;top:487px;width:108px;height:34px;background:var(--pink);color:#fff;font-size:12px;text-align:center;line-height:34px;border-radius:2px}

/* welcome */
.welcome h2{position:absolute;top:860px;left:0;width:1200px;text-align:center;font-family:"Roboto",sans-serif;font-weight:400;font-size:30px;color:#222}
.welcome h2 span{color:var(--pink)}
.welcome .intro{top:906px;text-align:center;font-size:11.5px;line-height:24px;color:#555}
.card{position:absolute;top:999px;width:313px;height:366px;background:#fff;box-shadow:0 0 0 1px #ececec}
.card .photo{height:184px}
.card h3{font-family:"Roboto",sans-serif;font-weight:500;font-size:16px;text-align:center;margin-top:22px;color:#222}
.card p{font-size:11.5px;line-height:21px;text-align:center;color:#555;padding:0 14px;margin-top:8px}
.card .more{position:absolute;bottom:0;left:0;width:100%;height:44px;background:var(--card-foot);text-align:center;line-height:44px;color:var(--pink);font-size:12px}

/* team */
.team{position:absolute;top:1418px;left:0;width:1200px;height:535px;background:linear-gradient(180deg,#e8587a,#e06584)}
.team h2{position:absolute;top:68px;width:1200px;text-align:center;color:#fff;font-family:"Roboto",sans-serif;font-weight:400;font-size:30px;letter-spacing:1px}
.member{position:absolute;top:146px;width:234px;height:322px;border:2px solid rgba(255,255,255,.8);text-align:center;color:#fff}
.hex{clip-path:polygon(25% 3%,75% 3%,100% 50%,75% 97%,25% 97%,0 50%);margin:0 auto}
.member .hex{width:150px;height:150px;margin-top:22px;background:#fff;display:flex;align-items:center;justify-content:center}
.member .hex div{width:140px;height:140px}
.member h4{font-family:"Open Sans",sans-serif;font-weight:400;font-size:17px;margin-top:14px;letter-spacing:.5px}
.member .role{font-size:13px;margin-top:2px}
.member p{font-size:12px;line-height:19px;margin-top:8px;padding:0 14px}

/* testimonials */
.testi h2{position:absolute;top:2000px;width:1200px;text-align:center;font-family:"Roboto",sans-serif;font-weight:400;font-size:36px;color:#222}
.testi h2 span{color:var(--pink)}
.t-hex{position:absolute}
.play{position:absolute;left:375px;top:2165px;width:48px;height:48px;border-radius:50%;background:rgba(255,255,255,.75);display:flex;align-items:center;justify-content:center}
.quote{position:absolute;top:2318px;left:200px;width:800px;text-align:center;font-style:italic;font-size:12px;line-height:22px;color:#555}
.t-name{position:absolute;top:2402px;left:0;width:1200px;text-align:center;color:var(--pink);font-size:14px}
.t-name:before,.t-name:after{content:"";display:inline-block;width:46px;height:1px;background:var(--pink);vertical-align:middle;margin:0 14px}
.dots{position:absolute;top:2444px;left:540px;display:flex;gap:16px}
.dots i{width:10px;height:10px;border-radius:50%;border:1px solid #bbb;display:block}
.dots i.on{background:var(--pink);border-color:var(--pink)}

/* footer */
.footer{position:absolute;top:2512px;left:0;width:1200px;height:279px;background:var(--dark);color:#fff}
.f-col{position:absolute;top:40px;font-size:12.5px;line-height:24px}
.f-col h5{font-family:"Roboto",sans-serif;font-weight:400;font-size:15px;letter-spacing:.5px;margin-bottom:12px}
.f-brand{font-family:"Roboto",sans-serif;font-weight:500;font-size:24px;color:var(--pink);margin-bottom:14px}
.f-line{display:flex;align-items:center;gap:10px}
.socials{display:flex;gap:6px;margin-top:12px}
.socials i{width:20px;height:20px;border-radius:50%;border:1px solid #ccc;display:block}
.news-input{width:242px;height:42px;background:#fff;color:#333;font-size:11px;padding:11px 12px;margin-top:14px}
.news-btn{width:98px;height:40px;background:var(--pink);font-size:11px;text-align:center;line-height:40px;margin-top:14px}
.copy{position:absolute;top:2791px;left:0;width:1200px;height:53px;background:var(--pink);color:#fff;text-align:center;font-size:12px;line-height:53px}
</style>
</head>
<body>

<header class="topbar">
  <div class="contact-top">
    <span class="icon"><svg width="14" height="14" viewBox="0 0 24 24"><path fill="#fff" d="M6.6 10.8a15 15 0 0 0 6.6 6.6l2.2-2.2c.3-.3.7-.4 1-.2 1.1.4 2.3.6 3.6.6.6 0 1 .4 1 1V20c0 .6-.4 1-1 1A17 17 0 0 1 3 4c0-.6.4-1 1-1h3.5c.6 0 1 .4 1 1 0 1.3.2 2.5.6 3.6.1.3 0 .7-.2 1z"/></svg></span>
    <span>+1 585 555 0100 12<br>info@brightkeyrealty.com</span>
  </div>
  <div class="brand">Brightkey Realty</div>
  <div class="search">search<svg width="12" height="12" viewBox="0 0 24 24"><circle cx="10" cy="10" r="7" fill="none" stroke="#8a9098" stroke-width="3"/><path d="M15 15l7 7" stroke="#8a9098" stroke-width="3"/></svg></div>
</header>

<nav class="nav">
  <ul>
    <li class="home"><svg width="22" height="20" viewBox="0 0 24 22"><path fill="#fff" d="M12 1 1 11h3v10h6v-6h4v6h6V11h3z"/></svg></li>
    <li>ABOUT US</li><li>BUYING A HOME</li><li>SELLING A HOME</li><li>TESTIMONIALS</li><li>COMMUNITY</li><li>BLOG</li><li>SERVICES</li><li>CONTACT US</li>
  </ul>
</nav>

<section class="hero" role="img" aria-label="Photo of a large suburban two-storey house with a green front lawn">
  <div class="hero-caption">
    <h1>Brightkey Realty</h1>
    <p>Lorem ipsum dolor sit amet, consectetur adipiscing sed do eiusmod tempor incididunt ut labore</p>
  </div>
  <svg class="arrow" style="left:14px" width="20" height="40" viewBox="0 0 20 40"><path d="M16 4 4 20l12 16" fill="none" stroke="#fff" stroke-width="2"/></svg>
  <svg class="arrow" style="left:1140px" width="20" height="40" viewBox="0 0 20 40"><path d="M4 4l12 16L4 36" fill="none" stroke="#fff" stroke-width="2"/></svg>
  <form class="quick">
    <div class="quick-head"><h2>QUICK SEARCH</h2><p>Property Quick Search</p></div>
    <div class="field" style="top:194px"><label>Min Price *</label><div class="box">10000</div></div>
    <div class="field" style="top:245px"><label>Max Price *</label><div class="box">50000</div></div>
    <div class="field" style="top:296px"><label>Min SQFT *</label><div class="box">0</div></div>
    <div class="field" style="top:347px"><label>Bedrooms *</label><div class="box">2</div></div>
    <div class="field" style="top:398px"><label>Min Baths *</label><div class="box">0</div></div>
    <div class="field" style="top:449px"><label>City *</label><div class="box">Choose a City<svg width="8" height="5" viewBox="0 0 8 5"><path d="M0 0h8L4 5z" fill="#555"/></svg></div></div>
    <div class="btn">SEARCH</div>
  </form>
</section>

<section class="welcome">
  <h2>WELCOME TO <span>BRIGHTKEY REALTY</span></h2>
  <p class="wrap intro">We are a full service real estate brokerage located in Rochester, New York offering personalized real estate solutions to the greater Rochester area. It is our goal, to ensure that every client we serve is fully represented in all of their real estate transactions. At Brightkey Realty, we provide you with over 17years of proven real estate experience. We are committed to providing every client with a level of drive and energy to ensure our clients receive an excellent outcome.</p>

  <article class="card" style="left:99px">
    <div class="photo" role="img" aria-label="Photo of a couple shaking hands with an agent in front of a house" style="background:linear-gradient(160deg,#9fb6c9,#8c8476 50%,#5b8a3e)"></div>
    <h3>BUYERS AGENTS</h3>
    <p>Our primary role is as a buyers agent. When selected to represent you, we bring our many years of per-sonal property acquisition and skilled</p>
    <div class="more">READ MORE &nbsp;→</div>
  </article>
  <article class="card" style="left:444px">
    <div class="photo" role="img" aria-label="Photo of a grey two-storey house at dusk" style="background:linear-gradient(180deg,#7fa3d0,#8a8d94 55%,#5f636a)"></div>
    <h3>INFORMED DECISIONS</h3>
    <p>Our primary role is as a buyers agent. When selected to represent you, we bring our many years of per-sonal property acquisition and skilled</p>
    <div class="more">READ MORE &nbsp;→</div>
  </article>
  <article class="card" style="left:788px">
    <div class="photo" role="img" aria-label="Photo of a row of townhouses with a fence and lawn" style="background:linear-gradient(180deg,#4f8fd6,#c9bf96 55%,#5d9a3c)"></div>
    <h3>INVESTMENT PROPERTIES</h3>
    <p>Our primary role is as a buyers agent. When selected to represent you, we bring our many years of per-sonal property acquisition and skilled</p>
    <div class="more">READ MORE &nbsp;→</div>
  </article>
</section>

<section class="team">
  <h2>OUR TEAM</h2>
  <div class="member" style="left:99px"><div class="hex"><div class="hex" role="img" aria-label="Portrait of an agent" style="background:linear-gradient(180deg,#b9b4ad,#7e6f62)"></div></div><h4>Dana Whitford</h4><div class="role">Agents</div><p>Lorem ipsum dolor sit amet, consectetur adipiscing elit, sed do eiusmod tempor incididunt.</p></div>
  <div class="member" style="left:353px"><div class="hex"><div class="hex" role="img" aria-label="Portrait of an agent" style="background:linear-gradient(180deg,#9aa0a6,#3e4650)"></div></div><h4>Dana Whitford</h4><div class="role">Agents</div><p>Lorem ipsum dolor sit amet, consectetur adipiscing elit, sed do eiusmod tempor incididunt.</p></div>
  <div class="member" style="left:611px"><div class="hex"><div class="hex" role="img" aria-label="Portrait of an agent" style="background:linear-gradient(180deg,#eceae6,#c7b7a6)"></div></div><h4>Dana Whitford</h4><div class="role">Agents</div><p>Lorem ipsum dolor sit amet, consectetur adipiscing elit, sed do eiusmod tempor incididunt.</p></div>
  <div class="member" style="left:868px"><div class="hex"><div class="hex" role="img" aria-label="Portrait of an agent" style="background:linear-gradient(180deg,#eef1f4,#9fb6d6)"></div></div><h4>Dana Whitford</h4><div class="role">Agents</div><p>Lorem ipsum dolor sit amet, consectetur adipiscing elit, sed do eiusmod tempor incididunt.</p></div>
</section>

<section class="testi">
  <h2>Client <span>Video</span> Testimonials</h2>
  <div class="t-hex hex" role="img" aria-label="Client portrait" style="left:318px;top:2076px;width:148px;height:161px;background:linear-gradient(180deg,#d8dde2,#2e3540)"></div>
  <div class="t-hex hex" style="left:478px;top:2074px;width:212px;height:232px;background:#e9b3c0"></div>
  <div class="t-hex hex" role="img" aria-label="Video thumbnail of a client testimonial" style="left:482px;top:2078px;width:204px;height:224px;background:linear-gradient(180deg,#d9d4cc,#8aa2b8)"></div>
  <div class="play" style="left:560px"><svg width="18" height="20" viewBox="0 0 18 20"><path d="M2 1l15 9-15 9z" fill="#555"/></svg></div>
  <div class="t-hex hex" role="img" aria-label="Client portrait" style="left:701px;top:2076px;width:148px;height:161px;background:linear-gradient(180deg,#dfe3e6,#3a4d66)"></div>
  <p class="quote">“ Lorem ipsum dolor sit amet, consectetur adipiscing elit, sed do eiusmod tempor incididunt ut labore et dolore magna aliqua. Ut enim ad minim veniam, quis nostrud exercitation ullamco laboris nisi ut aliquip ex ea commodo consequat. Duis aute irure dolor in reprehenderit in voluptate velit esse cillum dolore eu fugiat nulla pariatur. Excepteur sint occaecat cupidatat non proident. ”</p>
  <div class="t-name">Marcus Hale</div>
  <div class="dots"><i></i><i></i><i class="on"></i><i></i><i></i></div>
</section>

<footer class="footer">
  <div class="f-col" style="left:99px">
    <div class="f-brand">Brightkey Realty</div>
    <div>PO BOX 5310 Rochester,<br>NY 14610</div>
    <div class="f-line" style="margin-top:6px"><svg width="14" height="14" viewBox="0 0 24 24"><path fill="#fff" d="M6.6 10.8a15 15 0 0 0 6.6 6.6l2.2-2.2c.3-.3.7-.4 1-.2 1.1.4 2.3.6 3.6.6.6 0 1 .4 1 1V20c0 .6-.4 1-1 1A17 17 0 0 1 3 4c0-.6.4-1 1-1h3.5c.6 0 1 .4 1 1 0 1.3.2 2.5.6 3.6.1.3 0 .7-.2 1z"/></svg>585 555.0142</div>
    <div style="padding-left:24px">585 555.0187 (fax)</div>
    <div class="f-line"><svg width="14" height="12" viewBox="0 0 24 18"><rect x="1" y="1" width="22" height="16" fill="none" stroke="#fff" stroke-width="2"/><path d="M1 1l11 9 11-9" fill="none" stroke="#fff" stroke-width="2"/></svg>office@brightkeyrealty.com</div>
  </div>
  <div class="f-col" style="left:379px">
    <h5>QUICK LINKS</h5>
    <div>About<br>Blog<br>Buying a Home<br>Selling a Home<br>Real Estate in a Nutshell<br>Contact<br>Services</div>
  </div>
  <div class="f-col" style="left:601px">
    <h5>RESOURCES</h5>
    <div>Why use a buyers agent (PDF)<br>On the road to credit recovery (PDF)<br>Disclosure (PDF)<br>New Client PreScreen (PDF)</div>
    <div class="socials"><i></i><i></i><i></i><i></i></div>
  </div>
  <div class="f-col" style="left:859px">
    <h5>JOIN OUR NEWSLETTER</h5>
    <div style="font-size:11.5px;line-height:20px;width:240px">Excepteur sint occaecat cupidatat non proident, sunt in culpa qui</div>
    <div class="news-input">Enter Name</div>
    <div class="news-btn">SUBSCRIBE</div>
  </div>
</footer>
<div class="copy">Copyright 2016 | All Rights Reserved -- Brightkey Realty LLC</div>

</body>
</html>
```